Update Law Firm Website

Update law firm website pages, add pages for employees. Current website looks stale. www.lowrevanlaw.com

Target Market(s)

Personal injury clients

Industry/Entity Type

Legal

Number of Pages Required

5+ page

Font styles to use
Serif

Requirements
Must have
• User friendly and engaging design
Nice to have
• ?
Should not have
• scales of justice, law books,

```html
<!DOCTYPE html>
<html lang="en">
<head>
<meta charset="utf-8">
<title>Keystone Injury Law Group</title>
<link href="https://fonts.googleapis.com/css2?family=Libre+Baskerville:wght@400;700&family=Lato:wght@700;900&family=Ubuntu:wght@400;500;700&display=swap" rel="stylesheet">
<style>
:root{
  --gold:#fdca68;
  --gold-text:#f5c15f;
  --ink:#000;
  --text:#555;
  --muted:#777;
  --page:#f4f4f4;
  --card:#fff;
  --line:#d6d6d6;
}
*{margin:0;padding:0;box-sizing:border-box}
html,body{width:681px;height:1200px;overflow:hidden;background:var(--page)}
body{position:relative;font-family:"Ubuntu",sans-serif;color:var(--text)}
.abs{position:absolute}
.serif{font-family:"Libre Baskerville",serif}
.card{left:43px;top:43px;width:595px;height:1113px;background:var(--card);box-shadow:0 0 4px rgba(0,0,0,.15)}
.brand{left:50px;top:58px;font-size:13.6px;color:var(--ink);letter-spacing:.2px}
.brand-sub{left:115px;top:77px;font-size:7.2px;color:var(--gold-text)}
.call{right:52px;top:65px;font-size:12.5px;color:var(--gold-text);white-space:nowrap;text-align:right}
.call b{font-family:"Ubuntu",sans-serif;font-weight:700;color:var(--ink);font-size:16px}
.nav{left:50px;top:101px;width:581px;height:35px;background:var(--ink);overflow:hidden}
.nav a{position:absolute;top:0;line-height:35px;font-size:8.2px;color:#fff;text-decoration:none;white-space:nowrap}
.nav a.active{background:var(--gold);color:var(--ink);left:0;width:52px;text-align:center}
.hero{left:50px;top:136px;width:581px;height:295px;background:linear-gradient(90deg,#dfe6ea 0%,#c9d2d8 45%,#6f767c 72%,#3d4348 100%)}
.hero-title{left:58px;top:222px;font-family:"Lato",sans-serif;font-weight:900;font-size:29px;color:var(--ink);letter-spacing:-.5px}
.hero-text{left:59px;top:261px;font-size:8.4px;font-style:italic;color:#222;line-height:16.5px;width:385px}
.btn{background:var(--gold);color:var(--ink);font-family:"Libre Baskerville",serif;font-weight:700;border-radius:3px;text-align:center;white-space:nowrap}
.quote{left:58px;top:297px;width:141px;height:34px;line-height:34px;font-size:11.5px}
.dots{left:318px;top:405px;display:flex;gap:4px}
.dots i{width:7px;height:7px;border-radius:50%;background:var(--ink)}
.dots i.on{background:var(--gold)}
.sec-title{font-family:"Libre Baskerville",serif;font-size:20.5px;color:var(--ink)}
.sec-title span{color:var(--gold-text)}
.services-title{left:0;width:681px;top:463px;text-align:center}
.services-text{left:90px;width:501px;top:497px;text-align:center;font-size:8.2px;line-height:15.5px}
.tile{top:537px;width:136px;height:133px}
.tile .ph{height:97px}
.tile .label{height:36px;background:var(--ink);color:#fff;font-family:"Libre Baskerville",serif;font-weight:700;font-size:8.2px;line-height:36px;text-align:center;white-space:nowrap;overflow:hidden}
.eval{left:234px;top:678px;width:203px;height:32px;line-height:32px;font-size:11.5px}
.about-photo{left:50px;top:750px;width:117px;height:144px;background:linear-gradient(#ededed,#cfcfcf)}
.about-photo .ph{position:absolute;left:20px;top:18px;width:74px;height:83px;background:linear-gradient(#4a4a4a,#1c1c1c)}
.about-photo .name{position:absolute;left:0;bottom:0;width:117px;height:26px;line-height:26px;background:var(--gold);color:var(--ink);font-family:"Libre Baskerville",serif;font-weight:700;font-size:10px;text-align:center}
.about-title{left:181px;top:744px}
.about-name{left:182px;top:772px;font-size:10.5px;color:#333}
.about-text{left:184px;top:792px;width:208px;font-size:7.4px;line-height:15.3px}
.about-more{left:50px;top:906px;width:350px;font-size:7.9px;line-height:15.3px;color:var(--muted)}
.know{left:50px;top:941px;width:100px;height:32px;line-height:32px;font-size:11.5px}
.consult{left:413px;top:749px;width:218px;height:236px;border:1px solid var(--gold)}
.consult .banner{position:absolute;left:-1px;top:-1px}
.consult h3{position:absolute;left:0;width:216px;top:14px;text-align:center;font-family:"Libre Baskerville",serif;font-weight:700;font-size:12.4px;color:var(--ink)}
.consult p{position:absolute;left:12px;width:192px;top:63px;text-align:center;font-size:8.2px;line-height:14.5px;color:#444}
.field{position:absolute;left:12px;width:195px;height:23px;border:1px solid var(--line);font-size:7.8px;line-height:21px;padding-left:7px;color:#555}
.field .caret{position:absolute;right:7px;top:8px}
.submit{left:73px;top:200px;width:77px;height:29px;line-height:29px;font-size:11px;position:absolute}
.footer{left:50px;top:1020px;width:581px;height:130px;background:var(--ink)}
.fnav a{position:absolute;top:18px;font-size:7.6px;color:#fff;text-decoration:none;white-space:nowrap;line-height:24px}
.fnav a.active{left:3px;width:41px;background:var(--gold);text-align:center;border-radius:2px}
.social{position:absolute;top:12px;width:24px;height:24px;border-radius:50%;border:1px solid var(--gold)}
.social.fill{background:var(--gold)}
.fdiv{position:absolute;left:0;top:50px;width:581px;height:1px;background:#2a2a2a}
.fcontact{position:absolute;left:8px;top:61px;font-family:"Libre Baskerville",serif;font-size:11.5px;color:var(--gold-text)}
.ficon{position:absolute;top:81px;width:27px;height:27px;border-radius:50%;border:1px solid var(--gold)}
.ficon.fill{background:var(--gold)}
.ficon svg{position:absolute;left:50%;top:50%;transform:translate(-50%,-50%)}
.ftext{position:absolute;font-size:7.6px;line-height:12.8px;color:#fff}
.copy em{color:var(--gold);font-weight:700}
</style>
</head>
<body>
<div class="abs card"></div>

<div class="abs brand serif">KEYSTONE INJURY LAW GROUP</div>
<div class="abs brand-sub serif">DANIEL R. MOREAU, ESQUIRE</div>
<div class="abs call serif">Call Us Today <b>(555) 410-2280</b></div>

<nav class="abs nav">
  <a class="active" href="#">HOME</a>
  <a href="#" style="left:60px">SLIP AND FALL</a>
  <a href="#" style="left:131px">AUTO ACCIDENT</a>
  <a href="#" style="left:208px">CONSTRUCTION INJURIES</a>
  <a href="#" style="left:321px">MEDICAL MALPRACTICE</a>
  <a href="#" style="left:430px">RESULT</a>
  <a href="#" style="left:475px">ABOUT US</a>
  <a href="#" style="left:528px">CONTACT US</a>
</nav>

<div class="abs hero" role="img" aria-label="Attorney in a grey suit with arms crossed in a blurred conference room"></div>
<div class="abs hero-title">WE WILL HELP YOU</div>
<div class="abs hero-text">We help for city transit, car and trucking accidents, injuries caused by toxic chemicals, slip and fall cases involving shopping centers and office buildings, and against insurance companies.</div>
<div class="abs btn quote">GET A FREE QUOTE</div>
<div class="abs dots"><i></i><i></i><i class="on"></i><i></i></div>

<div class="abs sec-title services-title"><span>OUR</span> SERVICES</div>
<div class="abs services-text">Daniel R. Moreau is a Philadelphia Injury Lawyer who has successfully handled death and serious injury cases involving city transit, car and trucking accidents, injuries caused by toxic chemicals, slip and fall cases involving shopping</div>

<div class="abs tile" style="left:50px"><div class="ph" role="img" aria-label="Businessman slipping on a wet floor beside a caution sign" style="background:linear-gradient(#e2e2e0,#b8b8b4)"></div><div class="label">SLIP AND FALL</div></div>
<div class="abs tile" style="left:198px"><div class="ph" role="img" aria-label="Two cars after a collision" style="background:linear-gradient(135deg,#6f7a86,#2c3b58 55%,#8aa2bd)"></div><div class="label">AUTO ACCIDENT</div></div>
<div class="abs tile" style="left:346px"><div class="ph" role="img" aria-label="Injured worker in a safety vest lying on a construction site" style="background:linear-gradient(#a7a39c,#8a8c6e 60%,#c9cf5a)"></div><div class="label">CONSTRUCTION INJURIES</div></div>
<div class="abs tile" style="left:495px"><div class="ph" role="img" aria-label="Stethoscope and prescription pad on a desk" style="background:linear-gradient(135deg,#e8e4dc,#b78a5c 60%,#6b4526)"></div><div class="label">MEDICAL MALPRACTICE</div></div>

<div class="abs btn eval">GET YOUR CASE EVALUATION</div>

<div class="abs about-photo">
  <div class="ph" role="img" aria-label="Portrait of attorney Daniel R. Moreau"></div>
  <div class="name">Daniel R. Moreau</div>
</div>
<div class="abs sec-title about-title"><span>ABOUT</span> US</div>
<div class="abs about-name serif">Daniel R. Moreau</div>
<div class="abs about-text">Mr. Moreau has been twice selected as an Emerging Advocate, Regional Trial Review. He serves as a Judge Pro Tem and as an arbitrator for the Harbor County Civil Court, and is a member of the National Injury Counsel League and the State Injury Counsel Forum. He also serves as a Board Member for the Delaware Valley Trial Bar.</div>
<div class="abs about-more">Accidents, injuries caused by toxic chemicals, slip and fall cases involving shopping centers and office buildings, and against insurance companies.</div>
<div class="abs btn know">KNOW MORE</div>

<div class="abs consult">
  <svg class="banner" width="218" height="54" viewBox="0 0 218 54"><polygon points="0,0 218,0 218,30 109,54 0,30" fill="#fdca68"/></svg>
  <h3>FREE CONSULTATION</h3>
  <p>Fill out from below to request a call from one of Our Daniel R. Moreau</p>
  <div class="field" style="top:95px">Name*</div>
  <div class="field" style="top:121px">Email*</div>
  <div class="field" style="top:147px">Phone*</div>
  <div class="field" style="top:173px">Case*<svg class="caret" width="9" height="6" viewBox="0 0 9 6"><polygon points="0,0 9,0 4.5,6" fill="#555"/></svg></div>
  <div class="btn submit">SUBMIT</div>
</div>

<footer class="abs footer">
  <div class="fnav">
    <a class="active" href="#">Home</a>
    <a href="#" style="left:54px">Slip and Fall</a>
    <a href="#" style="left:111px">Auto Accident</a>
    <a href="#" style="left:172px">Construction Injuries</a>
    <a href="#" style="left:260px">Medical Malpractice</a>
    <a href="#" style="left:343px">Results</a>
    <a href="#" style="left:381px">About Us</a>
    <a href="#" style="left:425px">Contact Us</a>
  </div>
  <span class="social fill" style="left:496px"></span>
  <span class="social" style="left:524px"></span>
  <span class="social" style="left:552px"></span>
  <div class="fdiv"></div>
  <div class="fcontact">Contact Us</div>

  <span class="ficon fill" style="left:4px"><svg width="10" height="13" viewBox="0 0 10 13"><path d="M5 0a5 5 0 0 1 5 5c0 3.5-5 8-5 8S0 8.5 0 5a5 5 0 0 1 5-5z" fill="#fff"/><circle cx="5" cy="5" r="1.8" fill="#fdca68"/></svg></span>
  <div class="ftext" style="left:36px;top:84px">Daniel R. Moreau, Esquire 820<br>Harbor St #310 Philadelphia,<br>PA, 19107</div>

  <span class="ficon" style="left:156px"><svg width="9" height="14" viewBox="0 0 9 14"><rect x="0.7" y="0.7" width="7.6" height="12.6" rx="1.5" fill="none" stroke="#fdca68" stroke-width="1.3"/><circle cx="4.5" cy="11" r=".9" fill="#fdca68"/></svg></span>
  <div class="ftext" style="left:194px;top:84px">Call :<br><b>(555) 410-3190</b></div>

  <span class="ficon" style="left:307px"><svg width="13" height="10" viewBox="0 0 13 10"><rect x=".7" y=".7" width="11.6" height="8.6" rx="1" fill="none" stroke="#fdca68" stroke-width="1.2"/><path d="M1 1.2l5.5 4.3L12 1.2" fill="none" stroke="#fdca68" stroke-width="1.2"/></svg></span>
  <div class="ftext" style="left:339px;top:83px">Email :<br>info@keystoneinjurylaw.com</div>

  <div class="ftext copy" style="left:456px;top:88px">©2016 <em>Keystone Injury Law<br>Group</em> - All Right Reserved</div>
</footer>
</body>
</html>
```